verdant terraces simple classy business card design

my name is owen harlow and I run a gardening business aimed at high class verdant terraces. the business name is verdant terraces and our logo was designed on pixel forum .My clientel are anything from residential homes to businesses. I take pride in my work and know that I offer a service like no other in my area.
The business card will be used to represent my business and I want it to be not only rememberable, but simplistic and modern. Eye catching too. Of course I would like it relatable to gardening and appealing to the correct clientel - those being garden enthusiasts, prestigious homes and businesses that are after top of the line gardening services like no other on the market.
I am not a typical lawn mowing business so I don't want a typical card design that represents that. The gardens I work with are generally million dollar properties with owners who are very garden proud looking for upkeep and guidance from me along with sometimes whole new garden designs. I want the business cards to show to my clients that I take pride, as they do, in their garden. And I want them to know from my card that I am a professional, qualified horticulturist offering them a top of the line service for life. I want them to refer my business on. I want them to look at my business card and see class and professionalism in a modern unique bold way.
The card should be simple with the possibility of the logo on the front being embossed/debossed and my details on the back the card should have a organic garden feel it's very important to me that it is absolutely perfect
I am also very open to ideas and suggestions so look forward to seeing the designs. the business logo has been supplied with this project and I want the card to be double sided

Contact info is
Owen Harlow - Managing Director / Horticulturist
Phone : 0481 526 704
Email: owenharlow@verdantterraces.com.au

Target Market(s)

high class gardens residential and commercial

Industry/Entity Type

Gardener

Contact Information for Business Card

Contact info is
Phone : 0481 526 704

PLEASE MAKE CARD DOUBLE SIDED

Requirements
Must have
• organic simple classy modern feel
• must flow with the current logo that has been supplied with this project
• Double sided
• Must explain in a simple way that I deal with high end gardens and I'm a qualified horticulturist
Nice to have
• embossed debossed logo
Should not have
• shouldn't be to busy or cheap looking

```html
<!DOCTYPE html>
<html lang="en">
<head>
<meta charset="utf-8">
<title>Verdant Terraces – Business Card</title>
<link rel="stylesheet" href="https://fonts.googleapis.com/css2?family=Montserrat:wght@400&family=Noto+Serif:wght@400;700&family=Open+Sans:wght@400&display=swap">
<style>
  :root {
    --backdrop: #e9e6dc;
    --card: #f6f4ec;
    --card-edge: #e2ded0;
    --leaf: #5aa860;
    --ink: #2e2e2e;
    --muted: #7a7a7a;
    --deboss: #e3dfd2;
  }
  * { margin: 0; padding: 0; box-sizing: border-box; }
  html, body { width: 1200px; height: 802px; overflow: hidden; }
  body {
    background: var(--backdrop);
    display: flex;
    align-items: center;
    justify-content: center;
    gap: 48px;
  }
  .card {
    position: relative;
    width: 528px;
    height: 302px;
    background: var(--card);
    border: 1px solid var(--card-edge);
    box-shadow: 0 6px 18px rgba(0,0,0,0.12);
  }

  /* Back side: contact details */
  .identity {
    position: absolute;
    left: 34px;
    top: 34px;
    padding-left: 14px;
    border-left: 6px solid var(--leaf);
  }
  .identity__name {
    font-family: "Montserrat", sans-serif;
    font-weight: 400;
    font-size: 27px;
    color: var(--ink);
    line-height: 1.15;
  }
  .identity__role {
    font-family: "Noto Serif", serif;
    font-weight: 700;
    font-size: 16px;
    color: var(--leaf);
    line-height: 1.35;
  }
  .contact {
    position: absolute;
    left: 36px;
    bottom: 40px;
    list-style: none;
    font-family: "Open Sans", sans-serif;
    font-size: 15px;
    color: var(--muted);
  }
  .contact__item {
    display: flex;
    align-items: center;
    gap: 12px;
    margin-top: 8px;
  }
  .contact__icon { width: 18px; height: 16px; flex: none; }

  .brand {
    position: absolute;
    display: flex;
    align-items: center;
    gap: 10px;
    font-family: "Noto Serif", serif;
    font-weight: 400;
    text-transform: uppercase;
    letter-spacing: 0.08em;
    line-height: 1.15;
  }
  .brand__dot {
    border-radius: 50%;
    background: currentColor;
    flex: none;
  }
  .brand--back {
    right: 28px;
    bottom: 34px;
    font-size: 18px;
    color: var(--leaf);
  }
  .brand--back .brand__name { width: 118px; }
  .brand--back .brand__dot { width: 14px; height: 14px; }

  /* Front side: debossed mark */
  .card--front { display: flex; align-items: center; justify-content: center; }
  .brand--front {
    position: static;
    flex-direction: column;
    gap: 16px;
    font-size: 34px;
    color: var(--deboss);
  }
  .brand--front .brand__dot { width: 70px; height: 70px; }
</style>
</head>
<body>

  <section class="card card--back" aria-label="Card back">
    <div class="identity">
      <p class="identity__name">Owen Harlow</p>
      <p class="identity__role">Managing Director / Horticulturist</p>
    </div>

    <ul class="contact">
      <li class="contact__item">
        <svg class="contact__icon" viewBox="0 0 18 16" aria-hidden="true">
          <path d="M2 5 Q9 0 16 5 L14 7 L12 5 L6 5 L4 7 Z" fill="#5aa860"/>
          <rect x="3" y="8" width="12" height="7" rx="1.5" fill="#5aa860"/>
          <circle cx="9" cy="11.5" r="2" fill="#f6f4ec"/>
        </svg>
        <span>0481 526 704</span>
      </li>
      <li class="contact__item">
        <svg class="contact__icon" viewBox="0 0 18 16" aria-hidden="true">
          <rect x="1" y="3" width="16" height="11" rx="1" fill="#5aa860"/>
          <path d="M1.5 3.5 L9 9.5 L16.5 3.5" fill="none" stroke="#f6f4ec" stroke-width="1.4"/>
        </svg>
        <span>owenharlow@verdantterraces.com.au</span>
      </li>
    </ul>

    <div class="brand brand--back">
      <span class="brand__dot" aria-hidden="true"></span>
      <span class="brand__name">Verdant Terraces</span>
    </div>
  </section>

  <section class="card card--front" aria-label="Card front">
    <div class="brand brand--front">
      <span class="brand__dot" aria-hidden="true"></span>
      <span class="brand__name">Verdant Terraces</span>
    </div>
  </section>

</body>
</html>
```